We are a Dog Treat company that is going to sell a product that can be served frozen or room temp

Think about something similar to the mandarin oranges cups sold by brenvik. Our product needs to be sealed tight to maintain freshness. We want to sell the product in packs of 4, so a package would have 4 individual cups.
Each cup will contain around 3.5 ounces of product.

I have uploaded some packaging examples, and I uploaded our logo.

Target Market(s)

Dog owners, quorleta users, people who purchase dog food online

Industry/Entity Type

It Company

Requirements
Must have
• vacuum seal, logo on box
Nice to have
• logo on each cup

```html
<!DOCTYPE html>
<html lang="en">
<head>
<meta charset="utf-8">
<title>Velmora Mandarin Oranges – Cup Lids</title>
<link rel="stylesheet" href="https://fonts.googleapis.com/css2?family=Lilita+One&family=Oswald:wght@700&family=Roboto+Condensed:wght@700&display=swap">
<style>
  :root {
    --bg: #ececec;
    --rim-light: #f4f4f4;
    --rim-dark: #a9acb0;
    --peel: #f6a21b;
    --pith: #fff6e2;
    --flesh-light: #ffd670;
    --flesh: #f9b52c;
    --flesh-deep: #ee9212;
    --red: #e8231f;
    --brown: #4a2a17;
    --orange-text: #ef3e12;
    --white: #ffffff;
  }
  * { box-sizing: border-box; margin: 0; padding: 0; }
  html, body { width: 1200px; height: 928px; overflow: hidden; background: var(--bg); }
  .pack {
    width: 1200px;
    height: 928px;
    display: grid;
    grid-template-columns: repeat(2, 400px);
    grid-template-rows: repeat(2, 400px);
    gap: 24px 40px;
    justify-content: center;
    align-content: center;
  }
  .lid {
    position: relative;
    width: 400px;
    height: 400px;
    border-radius: 50%;
    background: linear-gradient(160deg, var(--rim-light), var(--rim-dark) 55%, var(--rim-light));
    padding: 12px;
  }
  .lid__label {
    position: relative;
    width: 100%;
    height: 100%;
    border-radius: 50%;
    background: var(--white);
    padding: 6px;
  }
  .lid__slice {
    width: 100%;
    height: 100%;
    border-radius: 50%;
    border: 7px solid var(--peel);
    background: radial-gradient(circle at 50% 50%, var(--flesh-light) 0 30%, var(--flesh) 62%, var(--flesh-deep) 92%, var(--pith) 96%);
  }
  .lid__text {
    position: absolute;
    inset: 0;
    display: flex;
    flex-direction: column;
    align-items: center;
    text-align: center;
    padding-top: 52px;
  }
  .claim-percent {
    font-family: "Roboto Condensed", sans-serif;
    font-weight: 700;
    font-size: 24px;
    line-height: 1;
    color: var(--red);
  }
  .claim-flavour {
    font-family: "Roboto Condensed", sans-serif;
    font-weight: 700;
    font-size: 15px;
    line-height: 1.2;
    color: var(--red);
  }
  .brand-badge {
    margin-top: 8px;
    width: 100px;
    height: 100px;
    border-radius: 50%;
    background: var(--white);
    display: flex;
    align-items: center;
    justify-content: center;
    font-family: "Lilita One", sans-serif;
    font-size: 20px;
    color: var(--brown);
  }
  .product-type {
    margin-top: 8px;
    font-family: "Roboto Condensed", sans-serif;
    font-weight: 700;
    font-size: 12px;
    color: var(--brown);
  }
  .brand-name {
    font-family: "Lilita One", sans-serif;
    font-weight: 400;
    font-size: 38px;
    line-height: 1.05;
    color: var(--brown);
  }
  .product-name {
    font-family: "Oswald", sans-serif;
    font-weight: 700;
    font-size: 18px;
    letter-spacing: 0.3px;
    color: var(--orange-text);
  }
</style>
</head>
<body>
<main class="pack">
  <section class="lid">
    <div class="lid__label">
      <div class="lid__slice" role="img" aria-label="Sliced mandarin orange cross-section"></div>
      <div class="lid__text">
        <p class="claim-percent">100%</p>
        <p class="claim-flavour">Orange Flavour</p>
        <div class="brand-badge">Velmora</div>
        <p class="product-type">DOG FOOD</p>
        <h2 class="brand-name">Velmora</h2>
        <p class="product-name">MANDARIN ORANGES</p>
      </div>
    </div>
  </section>
  <section class="lid">
    <div class="lid__label">
      <div class="lid__slice" role="img" aria-label="Sliced mandarin orange cross-section"></div>
      <div class="lid__text">
        <p class="claim-percent">100%</p>
        <p class="claim-flavour">Orange Flavour</p>
        <div class="brand-badge">Velmora</div>
        <p class="product-type">DOG FOOD</p>
        <h2 class="brand-name">Velmora</h2>
        <p class="product-name">MANDARIN ORANGES</p>
      </div>
    </div>
  </section>
  <section class="lid">
    <div class="lid__label">
      <div class="lid__slice" role="img" aria-label="Sliced mandarin orange cross-section"></div>
      <div class="lid__text">
        <p class="claim-percent">100%</p>
        <p class="claim-flavour">Orange Flavour</p>
        <div class="brand-badge">Velmora</div>
        <p class="product-type">DOG FOOD</p>
        <h2 class="brand-name">Velmora</h2>
        <p class="product-name">MANDARIN ORANGES</p>
      </div>
    </div>
  </section>
  <section class="lid">
    <div class="lid__label">
      <div class="lid__slice" role="img" aria-label="Sliced mandarin orange cross-section"></div>
      <div class="lid__text">
        <p class="claim-percent">100%</p>
        <p class="claim-flavour">Orange Flavour</p>
        <div class="brand-badge">Velmora</div>
        <p class="product-type">DOG FOOD</p>
        <h2 class="brand-name">Velmora</h2>
        <p class="product-name">MANDARIN ORANGES</p>
      </div>
    </div>
  </section>
</main>
</body>
</html>
```